Rings and things/plans. Wedding planning checklist design

We are a wedding videography start-up that's about to launch a chatterly campaign. We need a simple yet premium looking design to showcase a wedding planning checklist which we have written. The main focus of the design should be:

- On A4 pages
- Appeal to young engaged women
- Anyone at home can print it off and stick it onto a fridge
- Premium looking

The contents doesn't have to be on one piece of A4, the list can span more than one page. Also, it doesn't have to be traditional folded brochure style, a full A4 sized list is preferred. The design will potentially be used in further A4 brochure style blog posts. The written checklist and our company logo is attached for reference.

Target Market(s)

Young engaged woman

Industry/Entity Type

Wedding

Requirements
Must have
• Simple and premium feel.
Nice to have
• flexible design that can be reused in the future for blog posts.

```html
<!DOCTYPE html>
<html lang="en">
<head>
<meta charset="utf-8">
<title>Rings &amp; Things – Wedding Planning Checklist</title>
<link rel="stylesheet" href="https://fonts.googleapis.com/css2?family=Oswald:wght@300;400&family=Parisienne&family=Open+Sans:wght@400&display=swap">
<style>
  :root {
    --blush: #fbe3da;
    --blush-soft: #fdf0ea;
    --rose: #e8a99a;
    --box: #f0c9bd;
    --ink: #3b3434;
    --muted: #4c4545;
    --dots: #6b6060;
    --paper: #ffffff;
  }
  * { box-sizing: border-box; margin: 0; padding: 0; }
  html, body { width: 849px; height: 1200px; overflow: hidden; background: var(--paper); }
  .page { position: relative; width: 849px; height: 1200px; background: var(--paper); overflow: hidden; font-family: "Open Sans", Arial, sans-serif; color: var(--ink); }

  .header-band { position: absolute; top: 0; left: 0; width: 100%; height: 61px; background: var(--blush); display: flex; justify-content: center; align-items: center; gap: 10px; }
  .brand-dot { width: 10px; height: 10px; border-radius: 50%; background: var(--rose); }
  .brand-name { font-family: "Oswald", Arial, sans-serif; font-weight: 300; font-size: 20px; color: var(--ink); }

  .footer-band { position: absolute; left: 0; bottom: 0; width: 100%; height: 17px; background: var(--blush); }

  .lace-decoration { position: absolute; top: 61px; right: 0; width: 250px; height: 1122px;
    background: radial-gradient(ellipse at 80% 30%, #fbeee9 0%, rgba(255,255,255,0) 60%),
                radial-gradient(ellipse at 70% 75%, #fbeee9 0%, rgba(255,255,255,0) 60%); }

  .photo-band { position: absolute; top: 303px; left: 0; width: 100%; height: 142px;
    background: linear-gradient(90deg, #cfc6c0 0%, #bfb3ab 30%, #d8a6b0 55%, #e6c3c6 70%, #c89aa6 85%, #b8aaa3 100%); }
  .photo-band-panel { position: absolute; top: 348px; left: 0; width: 441px; height: 84px; background: rgba(255,255,255,0.72); }

  .section-title { position: absolute; left: 0; width: 100%; text-align: center; }
  .section-rule { position: absolute; left: 264px; width: 322px; border-top: 2px dotted var(--dots); }
  .section-heading { font-family: "Parisienne", cursive; font-size: 46px; color: var(--rose); line-height: 1; }

  .task { position: absolute; width: 300px; }
  .task-check { position: absolute; left: -32px; top: 5px; width: 20px; height: 20px; border: 2px solid var(--box); background: var(--paper); }
  .task-title { font-family: "Oswald", Arial, sans-serif; font-weight: 300; font-size: 21px; line-height: 28px; color: var(--ink); }
  .task-note { font-size: 10.5px; line-height: 16px; color: var(--muted); margin-top: 3px; }
  .col-left { left: 83px; }
  .col-right { left: 513px; }
</style>
</head>
<body>
<div class="page">
  <header class="header-band">
    <span class="brand-dot"></span>
    <span class="brand-name">Rings &amp; Things</span>
  </header>

  <div class="lace-decoration" role="img" aria-label="Faint white lace pattern decoration"></div>

  <div class="section-rule" style="top:84px"></div>
  <div class="section-title" style="top:92px"><div class="section-heading">9 Months</div></div>
  <div class="section-rule" style="top:146px"></div>

  <div class="task col-left" style="top:173px">
    <span class="task-check"></span>
    <div class="task-title">Book your official videographers</div>
    <div class="task-note">Rings &amp; Things are the way to go! (LOL)</div>
  </div>
  <div class="task col-left" style="top:232px">
    <span class="task-check"></span>
    <div class="task-title">Book your photographer</div>
    <div class="task-note">Consider having an unplugged wedding</div>
  </div>
  <div class="task col-right" style="top:173px">
    <span class="task-check"></span>
    <div class="task-title">Book your celebrant</div>
    <div class="task-note">Have some good conversations with them<br>to determine if they're the right fit</div>
  </div>

  <div class="photo-band" role="img" aria-label="Photo of pink roses lying on weathered wooden boards"></div>
  <div class="photo-band-panel"></div>
  <div class="task col-left" style="top:354px;width:340px">
    <span class="task-check"></span>
    <div class="task-title">Book your DJ, florist, caterer, decorator &amp;<br>wedding cake</div>
    <div class="task-note" style="white-space:nowrap">Use your friends circle! (Friends as vendors) This can be a big cost-cutter</div>
  </div>

  <div class="section-rule" style="top:491px"></div>
  <div class="section-title" style="top:501px"><div class="section-heading">6 Months</div></div>
  <div class="section-rule" style="top:555px"></div>

  <div class="task col-left" style="top:579px">
    <span class="task-check"></span>
    <div class="task-title">Buy wedding party suits/dresses</div>
    <div class="task-note">Your bridal party should complement your gown/<br>suit, but be sure to consider figure types and coloring<br>when selecting outfits</div>
  </div>
  <div class="task col-left" style="top:673px">
    <span class="task-check"></span>
    <div class="task-title">Book wedding car</div>
    <div class="task-note">Try and book this as soon as you can to ensure<br>you get the car of your dreams</div>
  </div>
  <div class="task col-left" style="top:750px">
    <span class="task-check"></span>
    <div class="task-title">Get your engagement photos done</div>
    <div class="task-note">These can be used for your save-the-date<br>cards. It's also the perfect time to test out your<br>photographer before the big day</div>
  </div>
  <div class="task col-right" style="top:580px">
    <span class="task-check"></span>
    <div class="task-title">Launch a website</div>
    <div class="task-note">A good way to broadcast your registry<br>details loud and clear</div>
  </div>
  <div class="task col-right" style="top:683px">
    <span class="task-check"></span>
    <div class="task-title">Finalise guest list</div>
    <div class="task-note">Try to avoid any last-minute add-ons. Don't let<br>your parents or in-laws bully you!</div>
  </div>

  <div class="section-rule" style="top:867px"></div>
  <div class="section-title" style="top:877px"><div class="section-heading">5 Months</div></div>
  <div class="section-rule" style="top:932px"></div>

  <div class="task col-left" style="top:956px">
    <span class="task-check"></span>
    <div class="task-title">Purchase dress and any other<br>accessories and shoes</div>
    <div class="task-note">These can include veils, hair pieces, jewellery.<br>But remember: less is more</div>
  </div>
  <div class="task col-left" style="top:1060px">
    <span class="task-check"></span>
    <div class="task-title">Send out the save-the-date notices</div>
    <div class="task-note">Send these as cards, chatterly notice or even as a video</div>
  </div>
  <div class="task col-right" style="top:959px">
    <span class="task-check"></span>
    <div class="task-title">Create a gift registry with at<br>least 3 retailers</div>
    <div class="task-note">Decide together on the things you need and want.<br>Make sure to be considerate of your guests and hit<br>all price points</div>
  </div>
  <div class="task col-right" style="top:1076px">
    <span class="task-check"></span>
    <div class="task-title">Plan your honeymoon</div>
    <div class="task-note">Don't forget to renew your passports!</div>
  </div>

  <div class="footer-band"></div>
</div>
</body>
</html>
```